business card design - photography

I am a fine art photographer. I would like to approach galleries to exhibit my work and need a business card.

The card should convey creativity and simplicity.
I would like a double sided card.

Some options:
1. An all white card with raised or embossed text or design to create a tactile finish.
2. a white and dark grey design would also work well.
3. Would be great to use my name as part of the design but not essential.
4. My name and title on the front, other details on the back of card.

The final design should be simple, minimal, elegant and innovative.
Being minimal, it will be more about texture, text size and placement.

examples of designs I would prefer provided here:
http://layoutmuse.net/ideas/40-plain-and-graceful-calling-card-layouts

I'm also open to other designs that may be unusual and unique.

Love this:
http://www.snapvault.com/pics/morningverses/583017264
Updates

I have uploaded a psd file after playing around in photoshop with various fonts.  I like the font (which I downloaded from typeshelf.net called Arual) but the design probably needs some refining.  I hope this helps.  If you'd like me to change the format of the file, please let me know.

Marta

Target Market(s)

Art Gallery owners/administrators and customers.

Industry/Entity Type

Business

Requirements
Must have
• A unique look.

Matte, silky finish or heavy textured stock. Double-sided card.

Front:
my name
photography by

Back:
phone no
email
web address
Nice to have
• Letterpress
embrossed
Clean fonts
Should not have
• Do not use illustrations of cameras or lenses.
No frames around the card edge.

```html
<!DOCTYPE html>
<html lang="en">
<head>
<meta charset="utf-8">
<title>Marta Rellick Photography – Business Card</title>
<link href="https://fonts.googleapis.com/css2?family=Inter:wght@400;700;800&display=swap" rel="stylesheet">
<style>
  :root {
    --page: #ffffff;
    --card: #ffffff;
    --edge: #7a7b7d;
    --ink: #6d6e70;
    --monogram: #eceded;
  }
  * { margin: 0; padding: 0; box-sizing: border-box; }
  html, body {
    width: 1200px;
    height: 354px;
    overflow: hidden;
    background: var(--page);
    font-family: "Inter", Helvetica, Arial, sans-serif;
  }
  .sheet { position: relative; width: 1200px; height: 354px; }
  .card {
    position: absolute;
    top: 0;
    width: 579px;
    height: 354px;
    background: var(--card);
    border: 1.5px solid var(--edge);
    overflow: hidden;
  }
  .card--front { left: 0; }
  .card--back { left: 621px; }

  .monogram {
    position: absolute;
    font-weight: 800;
    font-size: 560px;
    line-height: 1;
    letter-spacing: -30px;
    color: var(--monogram);
    white-space: nowrap;
    user-select: none;
  }
  .card--front .monogram { left: -150px; top: -70px; }
  .card--back .monogram { left: -330px; top: -20px; }

  .identity {
    position: absolute;
    left: 166px;
    top: 4px;
    color: var(--ink);
  }
  .identity__name {
    font-weight: 700;
    font-size: 64px;
    letter-spacing: -3.2px;
    line-height: 1.05;
  }
  .identity__title {
    font-weight: 400;
    font-size: 14px;
    line-height: 1;
    margin-top: -2px;
    margin-left: 2px;
  }

  .contact {
    position: absolute;
    right: 10px;
    top: 6px;
    list-style: none;
    text-align: right;
    color: var(--ink);
    font-size: 23px;
    line-height: 24px;
  }
  .contact__label { font-weight: 700; }
  .contact__value { font-weight: 400; }
</style>
</head>
<body>
  <main class="sheet">
    <section class="card card--front" aria-label="Card front">
      <div class="monogram" aria-hidden="true">MR</div>
      <header class="identity">
        <h1 class="identity__name">Marta Rellick</h1>
        <p class="identity__title">Photography</p>
      </header>
    </section>

    <section class="card card--back" aria-label="Card back">
      <div class="monogram" aria-hidden="true">MR</div>
      <ul class="contact">
        <li><span class="contact__label">t:</span> <span class="contact__value">0412 587 209</span></li>
        <li><span class="contact__label">e:</span> <span class="contact__value">mrellick@postmail.com</span></li>
        <li><span class="contact__label">w:</span> <span class="contact__value">www.martarellick.com</span></li>
      </ul>
    </section>
  </main>
</body>
</html>
```